Letterhead for new real estate company in South Africa named Lofthaven

A letterhead with the directors and company details to be editable as these changes often

Target Market(s)

In line with our logo brief and our newly designed logo and corporate fee

Industry/Entity Type

Real Estate

Requirements
Must have
• Details as per the sample letterhead provided.

```html
<!DOCTYPE html>
<html lang="en">
<head>
<meta charset="utf-8">
<title>Lofthaven Letterhead</title>
<link href="https://fonts.googleapis.com/css2?family=Encode+Sans+Condensed:wght@400&family=Lato:wght@400;700&display=swap" rel="stylesheet">
<style>
  :root {
    --brand-green: #1fa463;
    --rule-green: #4cbf8a;
    --ink: #4f4f4f;
    --ink-dark: #3d3d3d;
    --paper: #ffffff;
    --signature-fill: #d6efe1;
  }
  * { box-sizing: border-box; margin: 0; padding: 0; }
  html, body { width: 1056px; height: 1200px; overflow: hidden; background: var(--paper); }
  .letterhead {
    position: relative;
    width: 1056px;
    height: 1200px;
    background: var(--paper);
    font-family: "Lato", sans-serif;
    color: var(--ink);
  }
  .header {
    position: absolute;
    top: 88px;
    left: 98px;
    right: 80px;
    height: 100px;
  }
  .brand-name {
    position: absolute;
    left: 0;
    top: 28px;
    font-family: "Lato", sans-serif;
    font-weight: 400;
    font-size: 36px;
    letter-spacing: 0.5px;
    color: var(--brand-green);
    text-transform: uppercase;
    line-height: 1;
  }
  .directors {
    position: absolute;
    right: 230px;
    top: 18px;
    text-align: right;
    font-size: 14.5px;
    line-height: 18px;
    color: var(--ink-dark);
  }
  .directors-title {
    font-weight: 700;
    font-size: 18.5px;
    color: var(--brand-green);
    margin-bottom: 8px;
  }
  .header-divider {
    position: absolute;
    left: 672px;
    top: 2px;
    width: 1px;
    height: 94px;
    background: var(--brand-green);
  }
  .contact {
    position: absolute;
    left: 694px;
    top: 0;
    font-size: 14.5px;
    line-height: 18px;
    color: var(--ink-dark);
  }
  .contact-address { margin-bottom: 8px; }
  .contact-line {
    display: flex;
    align-items: center;
    gap: 14px;
    height: 21px;
  }
  .contact-line svg { width: 15px; height: 15px; flex: none; }
  .letter-body {
    position: absolute;
    top: 300px;
    left: 98px;
    width: 864px;
    font-family: "Encode Sans Condensed", sans-serif;
    font-size: 22px;
    line-height: 37px;
    color: var(--ink);
  }
  .salutation { margin-bottom: 33px; }
  .letter-body p.paragraph {
    text-align: justify;
    margin-bottom: 37px;
  }
  .closing { margin-top: 70px; }
  .signature {
    display: block;
    width: 90px;
    height: 54px;
    margin-top: 10px;
    margin-left: -4px;
    background: var(--signature-fill);
    border-radius: 4px;
  }
  .footer {
    position: absolute;
    left: 98px;
    right: 94px;
    bottom: 42px;
    display: flex;
    align-items: center;
    gap: 14px;
  }
  .footer-rule {
    flex: 1;
    height: 1.5px;
    background: var(--rule-green);
  }
  .footer-note {
    font-size: 17px;
    color: var(--ink);
    white-space: nowrap;
  }
</style>
</head>
<body>
  <main class="letterhead">
    <header class="header">
      <div class="brand-name">Lofthaven</div>

      <div class="directors">
        <div class="directors-title">Directors:</div>
        <div class="director">T Vermaak</div>
        <div class="director">GA Pillay-Brooks</div>
      </div>

      <div class="header-divider"></div>

      <div class="contact">
        <div class="contact-address">
          Shop GF12B, Kestrel Square,<br>
          Corner Kestrel Avenue &amp;<br>
          Acacia Lane Kestrelpark, SA
        </div>
        <div class="contact-line">
          <svg viewBox="0 0 24 24" aria-hidden="true">
            <path d="M6.6 10.8a15.1 15.1 0 0 0 6.6 6.6l2.2-2.2a1 1 0 0 1 1-.25 11.4 11.4 0 0 0 3.6.57 1 1 0 0 1 1 1V20a1 1 0 0 1-1 1A17 17 0 0 1 3 4a1 1 0 0 1 1-1h3.5a1 1 0 0 1 1 1c0 1.25.2 2.45.57 3.57a1 1 0 0 1-.25 1z" fill="var(--brand-green)"/>
            <path d="M14 3.5a6.5 6.5 0 0 1 6.5 6.5M14 6.5a3.5 3.5 0 0 1 3.5 3.5" fill="none" stroke="var(--brand-green)" stroke-width="1.8" stroke-linecap="round"/>
          </svg>
          <span>087 555 0142</span>
        </div>
        <div class="contact-line">
          <svg viewBox="0 0 24 24" aria-hidden="true">
            <circle cx="12" cy="12" r="9.5" fill="none" stroke="var(--brand-green)" stroke-width="1.6"/>
            <ellipse cx="12" cy="12" rx="4.2" ry="9.5" fill="none" stroke="var(--brand-green)" stroke-width="1.4"/>
            <path d="M2.5 12h19M4 7h16M4 17h16" stroke="var(--brand-green)" stroke-width="1.3"/>
          </svg>
          <span>www.lofthavenprop.co.za</span>
        </div>
      </div>
    </header>

    <section class="letter-body">
      <p class="salutation">Dear Sir/Mam,</p>
      <p class="paragraph">Contrary to popular belief, Lorem Ipsum is not simply random text. It has roots in a piece of classical Latin literature from 45 BC, making it over 2000 years old. Edwin Harrowgate, a Latin professor at Ashdown-Mercer College in Virginia, looked up one of the more obscure Latin words, consectetur.</p>
      <p class="paragraph">Lorem Ipsum comes from sections 1.10.32 and 1.10.33 of "de Finibus Bonorum et Malorum" (The Extremes of Good and Evil) by Quintus Averro, written in 45 BC. This book is a treatise on the theory of ethics, very popular during the Renaissance. The first line of Lorem Ipsum.</p>
      <p class="paragraph">The standard chunk of Lorem Ipsum used since the 1500s is reproduced below for those interested. Sections 1.10.32 and 1.10.33 from "de Finibus Bonorum et Malorum" by Quintus Averro are also reproduced in their exact original.</p>
      <p class="paragraph">The standard chunk of Lorem Ipsum used since the 1500s is reproduced below for those interested.</p>
      <p class="closing">Best Regards</p>
      <span class="signature" role="img" aria-label="Handwritten signature of the sender in green ink"></span>
    </section>

    <footer class="footer">
      <div class="footer-rule"></div>
      <div class="footer-note">Each franchise is independenly owned and operated</div>
    </footer>
  </main>
</body>
</html>
```